Design einer ITK Unternehmensbroschüre  Grundlayouts mit Deckblatt gesucht
Design einer ITK Unternehmensbroschüre Grundlayouts mit Deckblatt gesucht
Zielgruppe
ITK Systemlösungen mit Schwerpunkt Kommunikationslösungen
Regionale kleine und mittelständische Unternehmen aus allen Branchen
Aufgabenstellung
Vorlage sollte für den Print und Email Versand vorbereitet sein (A4) als Unternehmensbroschüre, die Designlinie sollte bodenständig und innovativ ausgelegt sein.
Dieses Projekt ist als Projektstart zu bewerten und wird in ein eins zu eins Projekt mit erweiterten Budget fortgeführt.
Es soll dazu dienen ein Grundlayout mit Deckblatt zu erstellen um die richtige Linie / Partner zu finden.
Die Kreativität inklusive Aussuchen von passendem Bildmaterial wird vom Designer erwartet und durch Lizenzen im eins zu eins Projekt im Nachgang verrechnet.

```html
<!DOCTYPE html>
<html lang="de">
<head>
<meta charset="utf-8">
<title>Velnaris – IT-Infrastruktur</title>
<link href="https://fonts.googleapis.com/css2?family=Mulish:wght@400;600;700;800&display=swap" rel="stylesheet">
<style>
  :root{
    --backdrop:#e4e5e8;
    --paper:#f4f5f6;
    --paper-shade:#e6e7ea;
    --ink-heading:#1f2a38;
    --ink-body:#3e4652;
    --ink-soft:#5b636e;
    --rule:#9aa1ab;
    --photo-light:#c7d6e6;
    --photo-mid:#6d8fb4;
    --photo-deep:#2c4e78;
    --folio-dark:#27313d;
  }
  *{margin:0;padding:0;box-sizing:border-box}
  html,body{width:1200px;height:848px;overflow:hidden;background:var(--backdrop)}
  body{font-family:"Mulish",sans-serif;color:var(--ink-body)}
  .spread{position:absolute;left:30px;top:15px;width:1140px;height:818px;display:flex;box-shadow:0 4px 18px rgba(0,0,0,.12)}
  .page{position:relative;width:570px;height:818px;overflow:hidden}
  .page--left{background:linear-gradient(90deg,var(--paper) 80%,var(--paper-shade) 100%)}
  .page--right{background:linear-gradient(90deg,var(--paper-shade) 0%,var(--paper) 12%,#fafafb 55%,var(--paper) 100%)}

  .page-title{position:absolute;left:67px;top:78px;font-size:22px;font-weight:800;color:var(--ink-heading);letter-spacing:.2px}
  .intro{position:absolute;left:153px;top:125px;width:315px;font-size:10.8px;line-height:15.4px;text-align:justify;hyphens:auto;color:var(--ink-body)}

  .photo{position:absolute;left:0;top:331px;width:570px;height:487px;
    background:radial-gradient(ellipse at 70% 35%,var(--photo-light) 0%,var(--photo-mid) 45%,var(--photo-deep) 100%)}
  .photo-notch{position:absolute;left:0;top:0;width:570px;height:487px}

  .folio{position:absolute;bottom:8px;font-size:6px;padding:2px 3px;line-height:1}
  .folio--left{left:2px;background:var(--paper);color:var(--ink-soft)}
  .folio--right{right:8px;background:var(--folio-dark);color:#fff}

  .brand{position:absolute;left:380px;top:52px;display:flex;align-items:center;gap:8px;font-size:22px;font-weight:700;color:var(--ink-heading);letter-spacing:.5px}
  .brand-dot{width:12px;height:12px;border-radius:50%;background:var(--ink-heading)}

  .section-head{position:absolute;font-size:11px;font-weight:700;color:var(--ink-heading);line-height:12px}
  .section-text{position:absolute;font-size:9.9px;line-height:14.55px;text-align:justify;hyphens:auto;color:var(--ink-soft)}
  .connector{position:absolute;left:0;top:0;width:570px;height:818px;pointer-events:none}

  .wlan-head{left:54px;top:80px}
  .wlan-text{left:54px;top:137px;width:227px}
  .net-head{left:387px;top:200px}
  .net-text{left:303px;top:270px;width:210px}
  .lte-head{left:54px;top:477px}
  .lte-text{left:173px;top:471px;width:342px}
  .lte-text p + p{margin-top:14px}
</style>
</head>
<body>
<div class="spread">
  <section class="page page--left">
    <h1 class="page-title">IT-INFRASTRUKTUR</h1>
    <p class="intro">Ein Firmennetzwerk ist das Fundament einer jeden Lösung in Ihrem Betrieb. Gerade in Zeiten der Digitalisierung ist es wichtig, sich für die richtige Lösung zu entscheiden und die Grundlage für Ihren technischen Erfolg zu schaffen. Unser KnowHow und langjährige Branchenkontakte ermöglichen es uns, Ihnen die volle Unterstützung bei Planung, Entwicklung, Implementierung sowie dem Betrieb intelligenter Netzwerktechnologien zu gewährleisten.</p>
    <div class="photo" role="img" aria-label="Bild: glänzendes Molekülmodell aus Kugeln und Stäben in Blautönen">
      <svg class="photo-notch" viewBox="0 0 570 487" aria-hidden="true">
        <polygon points="376,0 365,35 461,0" fill="var(--paper)"/>
      </svg>
    </div>
    <span class="folio folio--left">02</span>
  </section>

  <section class="page page--right">
    <div class="brand"><span class="brand-dot"></span>Velnaris</div>

    <svg class="connector" viewBox="0 0 570 818" aria-hidden="true">
      <polyline points="54,97 206,97 206,133" fill="none" stroke="var(--rule)" stroke-width=".7"/>
      <circle cx="206" cy="133" r="1.3" fill="var(--rule)"/>
      <line x1="382" y1="217" x2="382" y2="264" stroke="var(--rule)" stroke-width=".7"/>
      <circle cx="382" cy="264" r="1.3" fill="var(--rule)"/>
      <line x1="54" y1="497" x2="162" y2="497" stroke="var(--ink-heading)" stroke-width=".8"/>
      <circle cx="162" cy="497" r="1.3" fill="var(--rule)"/>
    </svg>

    <h2 class="section-head wlan-head">WLAN-Technologie</h2>
    <p class="section-text wlan-text">Ein stabiles und modernes WLAN Netz setzen Ihre Mitarbeiter, Kunden sowie mögliche IT-Lösungen heutzutage voraus. Zu einer sauberen Einrichtung gehört heutzutage mehr als nur die Einrichtung der Zugangspunkte. Um ein modernes und stabiles WLAN Netz zu gewährleisten, bieten wir Ihnen ein gut durchdachtes Konzept an. Eine Standortbegutachtung gehört für uns im Vorfeld zum Standard, eine Beobachtung der Gegebenheiten wie z.B. äußere Einflüsse, Ausstattung, Gebäudeeigenschaften sowie Funk-Alarmsysteme können das Ergebnis schmälern und zu Problemen führen. Aus diesem Grund bieten wir auch nach Implementierung standardmäßig eine zweite Standortbegutachtung an, um das installierte System im Livebetrieb punktuell zu verbessern. Zusammen mit unseren Technologiepartnern werden wir Ihren Nutzern ein Wohlfühlgefühl auf Ihre Endgeräte zaubern.</p>

    <h2 class="section-head net-head">Netzwerk-<br>Infrastruktur</h2>
    <p class="section-text net-text">Wir bieten Ihnen hochverfügbare Routing- und Switching-Lösungen mit leistungsstarken Komponenten und Verkabelungen als Basis. Auch Themen wie Standortvernetzung in Filialstrukturen bringen unser langjähriges KnowHow nicht ins Schwitzen. Mit unseren leistungsstarken Network Monitoring, Network Access Control (NAC) sowie Authentifizierungssystemen und Lösungen monitoren wir auf Wunsch Ihre komplette Netzwerkumgebung.</p>

    <h2 class="section-head lte-head">LTE-Technologie</h2>
    <div class="section-text lte-text">
      <p>Trotz des bundesweiten Ausbaus von Glasfasernetzen durch die zahlreichen großen Netzbetreiber sowie kleinen regionalen Carrier, kommt es immer noch vor, dass viele Firmen nicht genügend Bandbreite aufgrund fehlender Infrastrukturversorgung seitens der Carrier zur Verfügung steht. Meistens schlagen die Firmen sich mit teuren symmetrischen Kupfer Stand- oder SDSL-Leitungen mit geringen Bandbreiten für viel Geld rum. Nicht selten investieren die gleichen Firmen in ältere Techniken aufgrund der Bandbreite.</p>
      <p>Wir bieten mit unserer hausinternen FunkBrücke Pro Lösung hohe Bandbreiten im LTE Netz der führenden Carrier und veredeln unsere Lösung mit leistungsstarker Hardware sowie mit ausgefeilter Routingtechnik. So können wir unseren Kunden z.B. trotz LTE eine feste IP-Adresse anbieten, welche es Ihnen ermöglicht auch von außerhalb Ihres Netzwerks auf den Access, bzw. Router zuzugreifen. Unsere Lösung empfiehlt sich vor allem als Backup-Lösung sowie für kleinere Unternehmen, welche mehr Bandbreite benötigen, aber aufgrund der regionalen Infrastruktur keine bekommen.</p>
    </div>

    <span class="folio folio--right">03</span>
  </section>
</div>
</body>
</html>
```